Customer Value Leaflet

We need a bi-fold brochure designing, based on the attached PDF wireframes. Our company name is quillbrookery.com (of which the logo is currently being designed). The corporate colour is orange (the exact shade of which we are happy to leave to the designers discretion).

The leaflet will distributed to customer experience experts and marketers so the design needs to be bright, engaging, clean and simple. Design is critical.

```html
<!DOCTYPE html>
<html lang="en">
<head>
<meta charset="utf-8">
<title>Quillbrookery.com – Customer Value Leaflet</title>
<link rel="stylesheet" href="https://fonts.googleapis.com/css2?family=Poppins:wght@500;600;700&family=Questrial&display=swap">
<style>
  :root {
    --backdrop: #1e1e1e;
    --cover-brown: #a9521f;
    --paper: #ffffff;
    --orange: #e97f3f;
    --orange-text: #e8752f;
    --rust: #b95a22;
    --peach: #f6d2bd;
    --peach-ring: #f2c7ad;
    --apricot: #eea27a;
    --ink: #1a1a1a;
    --white: #ffffff;
  }
  * { margin: 0; padding: 0; box-sizing: border-box; }
  html, body { width: 1200px; height: 900px; overflow: hidden; background: var(--backdrop); }
  .canvas { position: relative; width: 1200px; height: 900px; }
  .artwork { position: absolute; left: 0; top: 0; }
  .back-cover-name {
    position: absolute; left: 150px; top: 396px; width: 380px;
    font: 700 33px/1 "Poppins", sans-serif; color: var(--white); letter-spacing: 0.5px;
  }
  .back-cover-phone {
    position: absolute; left: 166px; top: 446px;
    display: flex; align-items: center; gap: 12px;
    font: 600 37px/1 "Poppins", sans-serif; color: var(--white);
  }
  .phone-badge { width: 42px; height: 42px; }
  .back-cover-web {
    position: absolute; left: 70px; top: 757px; width: 537px; text-align: center;
    font: 600 20px/1 "Poppins", sans-serif; color: var(--white); letter-spacing: 0.5px;
  }
  .front-cover-name {
    position: absolute; left: 607px; top: 100px; width: 538px; text-align: center;
    font: 400 40px/1 "Questrial", sans-serif; color: var(--ink); letter-spacing: 1px;
  }
  .front-cover-tagline {
    position: absolute; left: 420px; top: 410px; width: 480px; height: 80px;
    transform: rotate(-90deg);
    font: 700 29px/38px "Poppins", sans-serif; color: var(--orange-text); letter-spacing: 1px;
  }
</style>
</head>
<body>
<main class="canvas">
  <svg class="artwork" width="1200" height="900" viewBox="0 0 1200 900" aria-hidden="false">
    <defs>
      <clipPath id="front-panel-clip"><rect x="607" y="68" width="538" height="760"/></clipPath>
      <clipPath id="back-panel-clip"><rect x="70" y="68" width="537" height="760"/></clipPath>
    </defs>

    <!-- back cover -->
    <rect class="back-cover" x="70" y="68" width="537" height="760" fill="var(--cover-brown)"/>
    <g class="back-cover-motifs" clip-path="url(#back-panel-clip)" fill="none" stroke="var(--white)" stroke-opacity="0.16" stroke-width="8" stroke-linecap="round" stroke-linejoin="round">
      <circle cx="420" cy="72" r="28" fill="var(--white)" fill-opacity="0.12" stroke="none"/>
      <path d="M110 420 h60 l-8 40 h-44 z"/>
      <path d="M175 495 h22 l14 50 h60 l12-38 h-78"/>
      <circle cx="220" cy="565" r="7" fill="var(--white)" fill-opacity="0.16"/>
      <circle cx="258" cy="565" r="7" fill="var(--white)" fill-opacity="0.16"/>
      <path d="M120 590 l48 14 -14 58 -48 -14 z"/>
      <path d="M290 620 h90 l-10 48 h-70 z M320 620 l24 -26"/>
      <path d="M110 800 l40 12 -10 30 -40 -12 z"/>
      <path d="M190 790 l40 10 -8 36 -40 -10 z"/>
    </g>
    <g class="back-cover-agent-marks" role="img" aria-label="Faint customer service agent motifs">
      <circle cx="100" cy="525" r="42" fill="var(--white)" fill-opacity="0.12"/>
      <circle cx="232" cy="672" r="48" fill="var(--white)" fill-opacity="0.12"/>
    </g>
    <text class="back-cover-network-mark" x="310" y="745" font-family="Poppins, sans-serif" font-weight="600" font-size="28" fill="var(--white)" fill-opacity="0.14">Chatterly</text>

    <!-- front cover -->
    <rect class="front-cover" x="607" y="68" width="538" height="760" fill="var(--paper)"/>
    <g class="front-cover-bubbles" clip-path="url(#front-panel-clip)">
      <path d="M700 560 C 820 470, 980 390, 1145 350" stroke="#d9e8f3" stroke-width="14" fill="none" opacity="0.6"/>
      <path d="M690 600 C 820 500, 990 430, 1145 410" stroke="#e6f0f7" stroke-width="10" fill="none" opacity="0.7"/>
      <circle cx="690" cy="830" r="82" fill="var(--peach)"/>
      <circle cx="1025" cy="815" r="30" fill="var(--peach)"/>
      <circle cx="1100" cy="180" r="35" fill="var(--peach)"/>
      <circle cx="822" cy="392" r="32" fill="var(--peach)"/>

      <circle cx="970" cy="420" r="122" fill="var(--peach-ring)"/>
      <circle cx="970" cy="420" r="110" fill="var(--rust)"/>

      <circle cx="1015" cy="283" r="118" fill="var(--peach-ring)"/>
      <circle cx="1015" cy="283" r="105" fill="var(--orange)"/>

      <circle cx="870" cy="692" r="110" fill="var(--peach-ring)"/>
      <circle cx="870" cy="692" r="98" fill="var(--rust)"/>

      <circle cx="1050" cy="662" r="110" fill="var(--peach-ring)"/>
      <circle cx="1050" cy="662" r="98" fill="var(--orange)"/>

      <circle cx="905" cy="527" r="112" fill="var(--peach-ring)"/>
      <circle cx="905" cy="527" r="100" fill="var(--orange)"/>

      <circle cx="1065" cy="520" r="86" fill="var(--peach-ring)"/>
      <circle cx="1065" cy="520" r="75" fill="var(--apricot)"/>
    </g>

    <!-- icons -->
    <g class="icon-cart" fill="none" stroke="var(--white)" stroke-width="6" stroke-linejoin="round" stroke-linecap="round">
      <path d="M968 258 h80 l-8 44 h-62 z"/>
      <path d="M1048 258 l6 -10 h12"/>
      <path d="M975 282 h70 M990 258 v44 M1005 258 v44 M1020 258 v44 M1035 258 v44"/>
      <path d="M978 302 l-2 12 h62"/>
      <circle cx="986" cy="323" r="7" fill="var(--white)"/>
      <circle cx="1040" cy="323" r="7" fill="var(--white)"/>
    </g>
    <g class="icon-basket">
      <path d="M908 512 l22 -26" stroke="var(--white)" stroke-width="8" stroke-linecap="round"/>
      <rect x="860" y="508" width="100" height="14" rx="5" fill="var(--white)"/>
      <path d="M868 524 h84 l-8 46 h-68 z" fill="var(--white)"/>
      <rect x="888" y="534" width="9" height="18" rx="4" fill="var(--orange)"/>
      <rect x="922" y="534" width="9" height="18" rx="4" fill="var(--orange)"/>
    </g>
    <g class="icon-receipt" fill="none" stroke="var(--white)" stroke-width="5" stroke-linejoin="round">
      <path d="M1055 485 l40 10 -14 56 -40 -10 z" fill="var(--white)" fill-opacity="0.25"/>
      <path d="M1042 545 c 5 10, 15 14, 45 14" />
      <path d="M1060 502 l22 6 M1057 514 l22 6 M1054 526 l22 6"/>
    </g>
    <g class="icon-agent" role="img" aria-label="Customer service agent icon">
      <circle cx="870" cy="692" r="46" fill="var(--white)" fill-opacity="0.9"/>
    </g>
    <text class="network-name" x="1050" y="670" text-anchor="middle" font-family="Poppins, sans-serif" font-weight="600" font-size="24" fill="var(--white)">Chatterly</text>
  </svg>

  <h2 class="back-cover-name">QUILLBROOKERY.COM</h2>
  <p class="back-cover-phone">
    <svg class="phone-badge" viewBox="0 0 42 42" aria-label="Phone">
      <rect width="42" height="42" rx="8" fill="var(--white)"/>
      <path d="M14 8 c-4 2 -6 5 -5 10 c2 8 7 14 15 16 c4 1 7 -1 9 -4 l-6 -6 l-4 3 c-4 -2 -7 -5 -8 -9 l3 -4 z" fill="var(--cover-brown)"/>
    </svg>
    <span class="phone-number">0845 000 3172</span>
  </p>
  <p class="back-cover-web">WWW.QUILLBROOKERY.COM</p>

  <h1 class="front-cover-name">QUILLBROOKERY.COM</h1>
  <p class="front-cover-tagline">BY PREDICTING CUSTOMER<br>LIFETIME VALUETODAY...</p>
</main>
</body>
</html>
```